依頼詳細
「仙台箪笥」は本来すべてが「手しごと」で作られたものを言います。しかし、近年は工場の機械で大量生産されたものを「仙台箪笥」として販売する企業が増えてきており、「本物」を作る職人達は価格競争で負けてしまいます。そんな中でも、柴崎庵では全ての工程を手しごとで行い、愚直に仙台箪笥を作り続けてきました。今のまま「安かろう、良かろう」の精神で仙台箪笥を販売する企業や、それを購入する消費者が増え続けてしまっては、江戸時代から培われてきた仙台の伝統が途絶えてしまいます。本チラシのデザインでは、そんな時代に警笛を鳴らすようなメッセージを込めて頂きたいと考えております。柴崎庵の代表・柴崎守氏からのメッセージや仙台箪笥の歴史を説明する資料を添付します。そちらを参考に、本物の箪笥の価値を伝えるデザインをして下さった方を採用とさせて頂きます。柴崎氏からの要望は2つあり、「『ずいぶんお堅い感じね』と言われるようなもの』」「伝統工芸をずっと続けてやっているんだなというイメージ」を意識してほしいとのことです。その他、何か質問があればどうぞお気軽にお問い合わせくださいませ。Mail→tokoharuwen@mailbox-demo.jp
記載項目
工房名/仙台箪笥 柴崎庵
住所/添付資料
電話番号/添付資料
ホームページURL・QRコード/現在HPリニューアル中のため、リニューアル完了後にこちらで入れ込みます。入れるスペースを分かるようにしておいてください。
キャッチコピー/デザインに合わせ、「依頼詳細」にある説明を参考に、心に刺さるコピーを入れてください。
写真/添付資料にある、柴崎守氏の写真と仙台箪笥の写真を中心に上手く組み合わせてデザインしてください。

〜コピー参考例〜
(コピーが浮かばなかった場合は、こちらのコピーの中から選んで入れてください。)

・一〇〇年先に繋ぎたい、一〇〇年前の財産
・本物しか作らない、「手しごと」の心
サイズ
A4
ページ数
片面
希望イメージ
シンプル 複雑
単色 カラフル
暗い 明るい
日常 高級
遊び心 厳粛
未来的 伝統的
女性的 男性的
希望する色
仙台箪笥の色にあった色を基調としてください。
納品ファイル
• イラストレーター形式 (.ai)
補足説明
現在リニューアル中ですが、こちらが現在の「柴崎庵」のホームページです。
http://homepage5.example-host.jp/shibasakian/
→ページ左上にあるロゴを使用できれば、デザインの中に入れ込んでほしいです
参考映像
https://www.videoshare-demo.jp/watch?v=Qw3rTz8LmNp
https://www.videoshare-demo.jp/watch?v=Vb6yHs2KoRd

柴崎氏ご本人に選んで頂きました。

この度は多数のご応募、誠にありがとうございました。どの作品も素晴らしいもので、一つに選ぶのが非常に難しかったです。またの機会にも、どうぞご応募頂ければ幸いです。宜しくお願い致します。

```html
<!DOCTYPE html>
<html lang="ja">
<head>
<meta charset="UTF-8">
<title>仙台箪笥 柴崎庵 チラシ</title>
<link rel="stylesheet" href="https://fonts.googleapis.com/css2?family=Shippori+Mincho+B1:wght@500;700;800&family=Noto+Serif+JP:wght@400;600&display=swap">
<style>
  :root {
    --paper: #f5f1e8;
    --ink: #2b211c;
    --crimson: #a0181c;
    --chest-dark: #150706;
    --chest-mid: #4a1712;
    --mark-green: #2f6a3c;
    --rule: #b9a98f;
    --photo-tone: #8c7a68;
  }
  * { margin: 0; padding: 0; box-sizing: border-box; }
  html, body { width: 878px; height: 1200px; overflow: hidden; background: var(--paper); }
  body { font-family: "Noto Serif JP", serif; color: var(--ink); position: relative; }

  .flyer { position: absolute; inset: 0; border: 1px solid var(--rule); }
  .flyer-frame { position: absolute; inset: 10px; border: 1px solid var(--rule); }

  .workshop-mark { position: absolute; left: 34px; top: 30px; display: flex; align-items: center; gap: 8px; }
  .workshop-mark .dot { width: 54px; height: 54px; border-radius: 50%; background: var(--mark-green); }
  .workshop-mark .name { font-family: "Shippori Mincho B1", serif; font-weight: 700; font-size: 16px; color: var(--mark-green); }

  .vertical { writing-mode: vertical-rl; text-orientation: upright; }

  .tagline-box { position: absolute; right: 46px; top: 22px; width: 40px; height: 168px; background: var(--crimson);
    color: #fff; font-family: "Shippori Mincho B1", serif; font-weight: 700; font-size: 22px;
    display: flex; align-items: center; justify-content: center; letter-spacing: 3px; }

  .headline { position: absolute; right: 92px; top: 80px; height: 620px; font-family: "Shippori Mincho B1", serif;
    font-weight: 800; font-size: 74px; color: var(--crimson); letter-spacing: 2px; line-height: 1; }

  .chest-photo { position: absolute; left: 88px; top: 100px; width: 520px; height: 530px;
    background: radial-gradient(ellipse at 45% 40%, var(--chest-mid) 0%, #2b0d0a 55%, var(--chest-dark) 100%); }
  .chest-shadow { position: absolute; left: 70px; top: 615px; width: 560px; height: 30px;
    background: radial-gradient(ellipse at center, rgba(0,0,0,0.25), rgba(0,0,0,0) 70%); }

  .about-label { position: absolute; left: 36px; top: 110px; font-family: "Shippori Mincho B1", serif; font-weight: 700;
    font-size: 15px; color: var(--crimson); border-left: 2px solid var(--crimson); padding-left: 4px; letter-spacing: 2px; }

  .about-text { position: absolute; left: 622px; top: 100px; height: 430px; width: 80px; font-size: 11.5px; line-height: 1.75; letter-spacing: 1px; }

  .message-body { position: absolute; left: 36px; top: 665px; width: 520px; height: 330px; font-size: 12px; line-height: 1.8; letter-spacing: 1px; }

  .craftsman { position: absolute; left: 596px; top: 660px; width: 254px; height: 440px; }
  .craftsman-title { position: absolute; right: 6px; top: 0; font-family: "Shippori Mincho B1", serif; font-weight: 700; font-size: 20px; color: var(--crimson); letter-spacing: 3px; }
  .craftsman-role { position: absolute; left: 10px; top: 4px; width: 44px; height: 44px; border-radius: 50%; border: 1px solid var(--crimson);
    color: var(--crimson); font-size: 10px; display: flex; align-items: center; justify-content: center; text-align: center; line-height: 1.2; }
  .craftsman-name { position: absolute; left: 64px; top: 12px; font-family: "Shippori Mincho B1", serif; font-weight: 700; font-size: 16px; }
  .craftsman-name small { font-family: "Noto Serif JP", serif; font-weight: 400; font-size: 9px; margin-left: 4px; color: #6b5e52; }
  .craftsman-photo { position: absolute; left: 0; top: 175px; width: 254px; height: 160px;
    background: linear-gradient(160deg, #b5a593 0%, var(--photo-tone) 55%, #54463a 100%); }
  .craftsman-caption { position: absolute; left: 0; top: 344px; width: 254px; font-size: 9.5px; line-height: 1.6; }

  .footer { position: absolute; left: 20px; right: 20px; top: 1112px; height: 72px; border-top: 1px solid var(--rule); }
  .footer-name { position: absolute; left: 10px; top: 14px; font-family: "Shippori Mincho B1", serif; font-weight: 700; font-size: 30px; color: var(--crimson); letter-spacing: 2px; }
  .footer-name .prefix { font-size: 20px; margin-right: 6px; }
  .footer-address { position: absolute; left: 12px; top: 56px; font-size: 8px; color: #4a3f36; }
  .footer-contact { position: absolute; left: 312px; top: 12px; font-size: 18px; font-weight: 600; letter-spacing: 0.5px; display: flex; align-items: center; gap: 4px; }
  .footer-contact svg { width: 16px; height: 16px; }
  .footer-url { position: absolute; left: 360px; top: 44px; font-size: 16px; font-weight: 600; }
  .qr-space { position: absolute; right: 10px; top: 14px; width: 48px; height: 48px; border: 1px solid var(--ink);
    display: flex; align-items: center; justify-content: center; font-size: 11px; }
</style>
</head>
<body>
<div class="flyer">
  <div class="flyer-frame"></div>

  <div class="workshop-mark"><span class="dot"></span><span class="name">柴崎庵</span></div>

  <div class="tagline-box vertical">本物の手仕事</div>
  <h1 class="headline vertical">一〇〇年先の財産</h1>

  <div class="chest-shadow"></div>
  <div class="chest-photo" role="img" aria-label="漆塗りに鉄金具を施した手しごとの仙台箪笥"></div>

  <div class="about-label vertical">仙台箪笥とは</div>
  <p class="about-text vertical">仙台箪笥は江戸末期より仙台藩で作られた指物です。欅の木地に漆を幾度も塗り重ね、手打ちの鉄金具で飾る堅牢な造りが特徴で、親から子へと受け継がれてきました。</p>

  <p class="message-body vertical">一つの箪笥ができあがるまでには、木地づくり、漆塗り、金具づくりと、それぞれの職人の手を幾度も通ります。木を選び、乾かし、組み上げ、漆を塗っては研ぎ、また塗る。鉄を打ち、模様を彫り、一枚ずつ金具を仕上げる。そのすべてに近道はありません。近年、機械で大量に作られた品が同じ名で売られるようになりました。安さだけで選ばれる時代が続けば、江戸から受け継がれてきた技は途絶えてしまいます。柴崎庵は、すべての工程を手しごとで行うことを守り続けてきました。百年使える箪笥は、百年先の家族へ渡す財産です。本物しか作らない、その心をどうか手に取って確かめてください。</p>

  <section class="craftsman">
    <h2 class="craftsman-title vertical">柴崎守氏の想い</h2>
    <div class="craftsman-role">代表<br>職人</div>
    <div class="craftsman-name">柴崎 守<small>Mamoru Shibasaki</small></div>
    <div class="craftsman-photo" role="img" aria-label="工房で作業する代表職人 柴崎守氏の写真"></div>
    <p class="craftsman-caption">柴崎庵代表。若くして父に師事し、木地から金具まで一貫した手しごとを続ける。伝統の技を次の世代へつなぐため、今日も工房に立つ。</p>
  </section>

  <footer class="footer">
    <div class="footer-name"><span class="prefix">仙台箪笥</span>柴崎庵</div>
    <div class="footer-address">〒980-0000 宮城県仙台市青葉区杉町二丁目八番地</div>
    <div class="footer-contact">
      <svg viewBox="0 0 16 16" aria-hidden="true"><path d="M4 1h3l1 4-2 1a8 8 0 0 0 4 4l1-2 4 1v3c0 1-1 2-2 2C7 14 2 9 2 3c0-1 1-2 2-2z" fill="var(--ink)"/></svg>
      電話：(022)555-0148　FAX：(022)555-0149
    </div>
    <div class="footer-url">http://homepage5.example-host.jp/shibasakian/</div>
    <div class="qr-space">QR</div>
  </footer>
</div>
</body>
</html>
```